Songs Cover Art. Song tittle DJ K - Keep The Floor Lit

Hey

I need a cover art for my songs. My genre is Big Room House/EDM music and my DJ name is DJ K. Song title is Keep The Floor Lit. I'm a producer and i need a designer to design all my cover art so that i will be able upload my song with a cover art. Do let me know if you have any questions.

Song Tittle: Keep The Floor Lit
Artist name: DJ K

Thanks

Industry/Entity Type

House

Requirements
Should not have
• Please dont make the design to colourful.

```html
<!DOCTYPE html>
<html lang="en">
<head>
<meta charset="UTF-8">
<title>DJ K – Keep The Floor Lit</title>
<link rel="stylesheet" href="https://fonts.googleapis.com/css2?family=Bangers&display=swap">
<style>
  :root {
    --stage: #f1f1f1;
    --cover-black: #03090b;
    --deep-teal: #06262c;
    --teal: #1fb9c9;
    --teal-light: #5fe6f2;
    --glow: rgba(64, 224, 240, 0.75);
    --white: #ffffff;
    --ink: #0a0a0a;
  }
  * { box-sizing: border-box; margin: 0; padding: 0; }
  html, body {
    width: 1200px;
    height: 848px;
    overflow: hidden;
    background: var(--stage);
  }
  .canvas {
    position: relative;
    width: 1200px;
    height: 848px;
  }
  .cover {
    position: absolute;
    left: 328px;
    top: 82px;
    width: 544px;
    height: 544px;
    overflow: hidden;
    background: var(--cover-black);
  }
  .cover-art {
    position: absolute;
    inset: 0;
    background:
      radial-gradient(ellipse 60% 8% at 50% 29%, rgba(220, 250, 255, 0.85), transparent 70%),
      radial-gradient(ellipse 55% 35% at 50% 28%, rgba(40, 190, 210, 0.55), transparent 75%),
      radial-gradient(circle at 50% 70%, rgba(20, 110, 125, 0.45), transparent 45%),
      linear-gradient(180deg, var(--deep-teal) 0%, #0b3a42 30%, #051a1f 60%, var(--cover-black) 100%);
  }
  .cover-title {
    position: absolute;
    inset: 0;
    display: flex;
    flex-direction: column;
    align-items: center;
    font-family: 'Bangers', cursive;
    line-height: 0.9;
    text-transform: uppercase;
  }
  .artist {
    margin-top: 112px;
    font-size: 82px;
    letter-spacing: 2px;
    color: var(--white);
    -webkit-text-stroke: 3px var(--ink);
    text-shadow: 0 0 10px rgba(255, 255, 255, 0.6);
  }
  .song {
    display: flex;
    flex-direction: column;
    align-items: center;
    color: var(--teal);
    -webkit-text-stroke: 2px #0d4a52;
    text-shadow: 0 0 6px var(--glow), 0 0 18px var(--glow);
  }
  .song-line-small {
    font-size: 64px;
    letter-spacing: 1px;
  }
  .song-line-large {
    font-size: 104px;
    letter-spacing: 2px;
    color: var(--teal-light);
  }
</style>
</head>
<body>
  <main class="canvas">
    <section class="cover">
      <div class="cover-art" role="img" aria-label="Dark teal club scene with glowing loudspeakers, neon light arcs and a bright city-light horizon"></div>
      <h1 class="cover-title">
        <span class="artist">DJ K.</span>
        <span class="song">
          <span class="song-line-small">Keep The</span>
          <span class="song-line-large">Floor</span>
          <span class="song-line-small">Lit</span>
        </span>
      </h1>
    </section>
  </main>
</body>
</html>
```